TAVRO Capital Group LLC a High Risk Big Rewards company for Rich Young Entrepreneurs

We would like a very modern, powerful in the eyes of our customers, modern, minimalist feel, financial gain. this business card is for young Rich entrepreneurs who want to invest money into High Risk, Big Rewards Businesses. The card Should sell the business!! let your creativity go Wild! I pick most of the designers for this project because of your BOLD Designs, I would like this card to be Bold, Modern, Minimalist, use as many effects in your graphic Artist Mind, Do not let the Financial sound of this business to make you think Conservative that's the last thing we are! if you have a lot of money and you want to play a risky market call US
Updates

Project Deadline Extended
Reason: have not received, enough designs to choose 1st and second place, sure I have received over 100 designs but it seems most designers are submitting every card they have ever made before and calling it mine, please we are looking for fresh ideas please!

Target Market(s)

Private Risky Investors

Industry/Entity Type

Financial

Contact Information for Business Card

powerful in the eyes of our customers,modern, minimalist feel

Font styles to use
Other font styles liked:
• Modern feeling fonts

Requirements
Must have
• The Company Name is TAVRO Capital Group LLC and it must be on the CARD
• My Name, title, Cell , email
• Delvin Ashcroft G.E.D.
• Managing Member
• 555.038.6195
• delvin@tavrocapitalgroup.example
Nice to have
• try a black thick plastic card with round corners with Delvin Ashcroft GED (make sure GED is smaller than name) just on one side of the card, and my phone number with out the icons and email on the other side, this card should look like a exclusive credit card or exclusive VIP card, something you would never loose

```html
<!DOCTYPE html>
<html lang="en">
<head>
<meta charset="utf-8">
<title>TAVRO Capital Group LLC — Business Card</title>
<link rel="stylesheet" href="https://fonts.googleapis.com/css2?family=Open+Sans:wght@400;600;700&display=swap">
<style>
  :root {
    --backdrop: #2a2a2c;
    --accent-red: #c8262d;
    --paper: #f3f3f3;
    --ink: #2b2b2b;
    --muted-light: #d8d8d8;
    --white: #ffffff;
  }
  * { margin: 0; padding: 0; box-sizing: border-box; }
  html, body {
    width: 1200px;
    height: 660px;
    overflow: hidden;
    background: var(--backdrop);
    font-family: "Open Sans", Arial, sans-serif;
  }
  .canvas {
    position: relative;
    width: 1200px;
    height: 660px;
    display: flex;
    align-items: center;
    justify-content: center;
  }
  .business-card {
    position: relative;
    width: 360px;
    height: 600px;
    border-radius: 6px;
    overflow: hidden;
    box-shadow: 0 14px 40px rgba(0, 0, 0, 0.45);
  }
  .card-art {
    position: absolute;
    inset: 0;
    width: 100%;
    height: 100%;
    display: block;
  }
  .company-name {
    position: absolute;
    left: 0;
    top: 150px;
    width: 100%;
    height: 80px;
    display: flex;
    align-items: center;
    justify-content: center;
    color: var(--white);
    font-weight: 700;
    font-size: 18px;
    letter-spacing: 0.5px;
    text-transform: uppercase;
  }
  .holder {
    position: absolute;
    right: 18px;
    top: 248px;
    text-align: right;
    color: var(--white);
    white-space: nowrap;
  }
  .holder-name {
    font-weight: 600;
    font-size: 14px;
    letter-spacing: 0.5px;
    text-transform: uppercase;
  }
  .holder-name .credential {
    font-size: 10.5px;
    letter-spacing: 0.3px;
  }
  .holder-title {
    font-size: 10px;
    font-weight: 400;
    color: var(--muted-light);
    margin-top: 1px;
  }
  .contact-list {
    position: absolute;
    right: 14px;
    top: 382px;
    width: 168px;
    list-style: none;
  }
  .contact-item {
    position: relative;
    text-align: right;
    color: var(--ink);
    line-height: 1;
  }
  .contact-item .contact-text {
    display: block;
    white-space: nowrap;
    padding-bottom: 5px;
    border-bottom: 1px solid var(--accent-red);
  }
  .contact-item.phone {
    margin-left: 30px;
    padding-right: 32px;
    font-size: 10.5px;
    margin-bottom: 24px;
  }
  .contact-item.email {
    padding-top: 22px;
    font-size: 8.5px;
  }
  .contact-icon {
    position: absolute;
    right: 0;
    top: -12px;
    width: 26px;
    height: 28px;
  }
  .contact-item.email .contact-icon {
    top: -8px;
  }
</style>
</head>
<body>
<main class="canvas">
  <article class="business-card">
    <svg class="card-art" viewBox="0 0 360 600" aria-hidden="true">
      <defs>
        <linearGradient id="darkFacets" x1="0" y1="0" x2="1" y2="1">
          <stop offset="0" stop-color="#303033"/>
          <stop offset="0.5" stop-color="#222224"/>
          <stop offset="1" stop-color="#2c2c2f"/>
        </linearGradient>
        <linearGradient id="redBand" x1="0" y1="0" x2="1" y2="0">
          <stop offset="0" stop-color="#c01f26"/>
          <stop offset="1" stop-color="#d9434a"/>
        </linearGradient>
        <linearGradient id="nameStrip" x1="0" y1="0" x2="1" y2="0">
          <stop offset="0" stop-color="#2a2a2c"/>
          <stop offset="1" stop-color="#3d3d40"/>
        </linearGradient>
      </defs>
      <g class="facet-texture" role="img" aria-label="Dark faceted low-poly texture">
        <rect x="0" y="0" width="360" height="600" fill="url(#darkFacets)"/>
      </g>
      <rect class="company-band" x="0" y="150" width="360" height="80" fill="url(#redBand)"/>
      <polygon class="name-strip" points="110,230 360,230 360,300 165,322" fill="url(#nameStrip)"/>
      <polygon class="contact-panel" points="165,322 360,300 360,600 185,600" fill="var(--paper)"/>
      <polyline class="divider-line" points="108,230 163,322 183,600" fill="none" stroke="var(--white)" stroke-width="4" stroke-linejoin="miter"/>
    </svg>

    <h1 class="company-name">TAVRO Capital Group LLC</h1>

    <div class="holder">
      <p class="holder-name">Delvin Ashcroft <span class="credential">G.E.D</span></p>
      <p class="holder-title">Managing Member</p>
    </div>

    <ul class="contact-list">
      <li class="contact-item phone">
        <span class="contact-text">555.038.6195</span>
        <svg class="contact-icon" viewBox="0 0 26 28" aria-hidden="true">
          <polygon points="13,1 25,7.5 25,20.5 13,27 1,20.5 1,7.5" fill="var(--accent-red)"/>
          <path d="M7 11.5c0-2 2.7-3.2 6-3.2s6 1.2 6 3.2v1.2h-3v-1.5h-6v1.5H7z" fill="var(--white)"/>
          <rect x="8.5" y="13.5" width="9" height="5.5" rx="1" fill="var(--white)"/>
        </svg>
      </li>
      <li class="contact-item email">
        <svg class="contact-icon" viewBox="0 0 26 28" aria-hidden="true">
          <polygon points="13,1 25,7.5 25,20.5 13,27 1,20.5 1,7.5" fill="var(--accent-red)"/>
          <rect x="7" y="9.5" width="12" height="9" rx="0.8" fill="var(--white)"/>
          <path d="M7.5 10l5.5 4.5 5.5-4.5" fill="none" stroke="var(--accent-red)" stroke-width="1.3"/>
        </svg>
        <span class="contact-text">delvin@tavrocapitalgroup.example</span>
      </li>
    </ul>
  </article>
</main>
</body>
</html>
```